Licensed Fabrication Operator Training Program

We need a flyer to advertise a training program to business. I will attach a rough draft "original file" that we need enhanced to look professional. Details to the program are here https://www.vornelskills.org/credentials/fabrication-credential-lfo/ We want it to look clean and professional.

Please use the information that is on the "original file" rough draft. I have attached an example pdf, the reason I don't like the example is because it has too many words and looks out of date.

Font styles to use
Serif
Sans Serif

```html
<!DOCTYPE html>
<html lang="en">
<head>
<meta charset="utf-8">
<title>Licensed Fabrication Operator Program</title>
<link href="https://fonts.googleapis.com/css2?family=Source+Sans+3:wght@400;600;700&display=swap" rel="stylesheet">
<style>
  :root{
    --ink-indigo:#2b2a8f;
    --ink-dark:#1c1c24;
    --band-navy:#283256;
    --band-violet:#4a3bbd;
    --paper:#eef0f8;
    --paper-lilac:#dcdcf0;
    --paper-mint:#e3f0ee;
    --footer-grey:#c2c2c4;
    --badge-silver:#b9bdc6;
    --badge-navy:#1f2c5c;
  }
  *{margin:0;padding:0;box-sizing:border-box}
  html,body{width:1200px;height:1200px;overflow:hidden;background:#fff}
  body{font-family:"Source Sans 3",sans-serif;position:relative}
  .flyer{
    position:absolute;left:245px;top:86px;width:709px;height:1044px;overflow:hidden;
    background:linear-gradient(160deg,var(--paper) 0%,var(--paper-lilac) 45%,var(--paper-mint) 70%,var(--paper) 100%);
  }
  .abs{position:absolute}
  .title{left:0;width:630px;top:40px;text-align:center;color:var(--ink-indigo);font-weight:700;font-size:29px;line-height:36px}
  .badge{left:569px;top:14px;width:112px;height:112px}
  .pillar-band{
    left:7px;top:129px;width:694px;height:63px;border-radius:32px;
    background:linear-gradient(90deg,var(--band-navy) 0%,var(--band-violet) 50%,var(--band-navy) 100%);
  }
  .pillar{position:absolute;top:0;height:63px;display:flex;align-items:center;justify-content:center;text-align:center;color:#fff;font-size:27px;line-height:31px;transform:translateX(-50%);white-space:nowrap}
  .visual{border-radius:6px}
  .trainer-a{left:127px;top:222px;width:244px;height:182px;background:radial-gradient(circle at 55% 50%,#8a93a6 0%,#b9bfcc 55%,rgba(200,205,220,0) 75%)}
  .trainer-b{left:399px;top:362px;width:268px;height:264px;background:radial-gradient(circle at 70% 25%,#3d6fc2 0%,#7c9ad0 22%,rgba(190,198,215,.9) 40%,#b5bac6 65%,rgba(200,205,220,0) 80%)}
  .highlights{left:343px;width:360px;top:240px;text-align:center;color:var(--ink-indigo);font-weight:700;font-size:24px;line-height:30px}
  .skills-heading{left:19px;top:377px;color:var(--ink-dark);font-weight:700;font-size:23px}
  .skills-list{left:19px;top:421px;list-style:none;color:var(--ink-dark);font-size:24px;line-height:30px}
  .terms{left:474px;top:652px;color:var(--ink-indigo);font-weight:700;font-size:23px;line-height:29.5px}
  .testimonial{left:190px;top:768px;width:512px;height:102px;border:1px solid #6a6a7a;padding:4px 6px;color:var(--ink-dark);font-size:15px;line-height:19px}
  .contact{left:13px;top:850px;font-size:19px;line-height:25px;font-weight:600;font-style:normal}
  .contact .lead{color:var(--ink-indigo)}
  .contact .detail{color:var(--ink-dark);font-weight:700}
  .partners{left:0;top:951px;width:709px;height:93px;background:var(--footer-grey)}
  .partners-caption{position:absolute;right:7px;top:1px;font-size:15.5px;color:var(--ink-dark)}
  .partner{position:absolute;top:54px;transform:translate(-50%,-50%);font-size:20px;font-weight:700;color:var(--ink-dark);white-space:nowrap;display:flex;align-items:center;gap:6px}
  .partner.stacked{font-size:14px;line-height:16px;text-align:center;white-space:normal;width:96px;justify-content:center}
  .partner .dot{width:12px;height:12px;border-radius:50%;background:var(--badge-navy)}
</style>
</head>
<body>
<main class="flyer">
  <h1 class="abs title">Licensed Fabrication Operator<br>Program</h1>

  <svg class="abs badge" viewBox="0 0 112 112" role="img" aria-label="Program credential seal">
    <circle cx="56" cy="56" r="54" fill="var(--badge-silver)"/>
    <circle cx="56" cy="56" r="40" fill="var(--badge-navy)"/>
  </svg>

  <nav class="abs pillar-band">
    <span class="pillar" style="left:88px">Safety</span>
    <span class="pillar" style="left:235px">Quality</span>
    <span class="pillar" style="left:386px">Process</span>
    <span class="pillar" style="left:551px">Maintenance<br>Awareness</span>
  </nav>

  <div class="abs visual trainer-a" role="img" aria-label="Photo of a mechanical training rig with blue motor and yellow wiring"></div>

  <p class="abs highlights">Advanced Manufacturing<br>Hands-On Learning<br>College Credits Eligible</p>

  <div class="abs visual trainer-b" role="img" aria-label="Photo of a blue control panel trainer beside an enclosed mechanical rig"></div>

  <h2 class="abs skills-heading">SKILLS TAUGHT</h2>
  <ul class="abs skills-list">
    <li>Communication</li>
    <li>Lean Principles</li>
    <li>Problem Solving</li>
    <li>Teamwork</li>
    <li>Locating Information</li>
    <li>Supply Chain &amp; Logistics</li>
    <li>Data Analysis</li>
    <li>Total Productive Maintenance</li>
    <li>Autonomous Maintenance</li>
    <li>Customer Sservice</li>
    <li>Project Management</li>
  </ul>

  <p class="abs terms">120 hours<br>$2,500 per students<br>WTP Reimbursement</p>

  <blockquote class="abs testimonial">”We feel that VSC LFO certification compliments not only the qualifications of the candidates we see, but also enhance the knowledge, skills, and abilities of existing team members in our pursuit of manufacturing excellence”- Dale Renwick Vice President &amp; General Manager Halvern Motor Works</blockquote>

  <address class="abs contact">
    <div class="lead">Call to schedule</div>
    <div class="detail">5550142876</div>
    <div class="detail">dale@northlineops.com</div>
    <div class="lead">On-site training available</div>
  </address>

  <footer class="abs partners">
    <p class="partners-caption">VSC Certification Scheme Committee Members Work at:</p>
    <span class="partner stacked" style="left:70px">Pelham Accreditation</span>
    <span class="partner" style="left:208px">Rowan Motors</span>
    <span class="partner" style="left:330px">Quellex</span>
    <span class="partner" style="left:463px"><span class="dot"></span>VSC</span>
    <span class="partner" style="left:600px"><span class="dot"></span>LFO</span>
  </footer>
</main>
</body>
</html>
```